Bref créative
Modern Real Estate Design
Modern Real Estate Business cards
Modern
Derek Ashworth
Team Leader/Realtor
4816 N Birchwood Plaza Suite 300
Midvale, UT, 84047
ashworthderek385@mailnest.example
derekashworthteam.example
I would like the card to be teal,white and grey. Also want to get design for presentation
folders. I have a sample of what I want it to look like that I can email if possible.
This is the style I'm looking for I made this and would like the cards and folders to use this look. Thanks
This is my logo. I will also need to put Summit 48 logo in the bottom corner of the card.
I need the S48 logo on card but not on anything else. Thanks

```html
<!DOCTYPE html>
<html lang="en">
<head>
<meta charset="utf-8">
<title>Derek Ashworth Team – Business Card</title>
<link rel="stylesheet" href="https://fonts.googleapis.com/css2?family=Montserrat:wght@400;600;700&family=Open+Sans:wght@400;600&display=swap">
<style>
  :root {
    --teal: #1a9e9c;
    --teal-dark: #12807e;
    --grey: #6d6e71;
    --grey-light: #c9cacc;
    --grey-band: #9a9b9e;
    --card: #ffffff;
    --backdrop: #e9eaec;
  }
  * { box-sizing: border-box; margin: 0; padding: 0; }
  html, body {
    width: 1200px; height: 900px; overflow: hidden;
    background: var(--backdrop);
  }
  .business-card {
    position: absolute;
    left: 100px; top: 164px;
    width: 1000px; height: 572px;
    background: var(--card);
    box-shadow: 0 10px 30px rgba(0,0,0,0.12);
    font-family: "Open Sans", sans-serif;
    color: var(--grey);
  }
  .brand {
    position: absolute; top: 70px; left: 0; width: 100%;
    text-align: center;
  }
  .brand-square {
    display: block; margin: 0 auto 16px;
    width: 78px; height: 78px; background: var(--teal);
  }
  .brand-name {
    font-family: "Montserrat", sans-serif;
    font-weight: 600; font-size: 42px; letter-spacing: 1px;
    color: var(--teal); line-height: 1;
  }
  .brand-url {
    margin-top: 10px; font-size: 15px; color: var(--grey);
  }
  .agent {
    position: absolute; top: 318px; left: 0; width: 100%;
    text-align: center;
  }
  .agent-name {
    font-family: "Montserrat", sans-serif;
    font-weight: 700; font-size: 22px; color: var(--teal);
  }
  .agent-title { font-size: 16px; margin-top: 4px; }
  .contact-row {
    position: absolute; left: 40px; right: 40px;
    display: flex; align-items: center; gap: 22px;
    font-size: 15.5px; white-space: nowrap;
  }
  .contact-row.primary { top: 395px; }
  .contact-row.secondary { top: 425px; }
  .contact-item { display: flex; align-items: center; gap: 7px; }
  .icon { width: 18px; height: 18px; flex: none; }
  .bottom-band {
    position: absolute; left: 0; right: 0; bottom: 44px; height: 24px;
    background: linear-gradient(to bottom, var(--grey-light), var(--grey-band));
  }
  .web-tab {
    position: absolute; left: 300px; width: 480px; bottom: 44px; height: 62px;
    background: var(--teal);
    border-radius: 12px 12px 0 0;
    display: flex; align-items: center; justify-content: center;
    color: #fff; font-size: 16px; letter-spacing: 3px;
  }
</style>
</head>
<body>
<div class="business-card">
  <div class="brand">
    <span class="brand-square"></span>
    <div class="brand-name">DEREK ASHWORTH TEAM</div>
    <div class="brand-url">derekashworthteam.example</div>
  </div>

  <div class="agent">
    <div class="agent-name">Derek Ashworth</div>
    <div class="agent-title">Team Leader/Realtor</div>
  </div>

  <div class="contact-row primary">
    <span class="contact-item">
      <svg class="icon" viewBox="0 0 20 20"><circle cx="10" cy="10" r="10" fill="var(--teal)"/><path d="M10 4a4 4 0 0 0-4 4c0 3 4 8 4 8s4-5 4-8a4 4 0 0 0-4-4zm0 5.5a1.5 1.5 0 1 1 0-3 1.5 1.5 0 0 1 0 3z" fill="#fff"/></svg>
      4816 N Birchwood Plaza Suite 300 Midvale, UT, 84047
    </span>
    <span class="contact-item">
      <svg class="icon" viewBox="0 0 20 20"><circle cx="10" cy="10" r="10" fill="var(--teal)"/><path d="M7 5l2 2.5-1.2 1.2a7 7 0 0 0 3.5 3.5L12.5 11l2.5 2-1.2 1.7C10 14.5 5.5 10 5.3 6.2z" fill="#fff"/></svg>
      801-555-0142
    </span>
    <span class="contact-item">
      <svg class="icon" viewBox="0 0 20 20"><circle cx="10" cy="10" r="10" fill="var(--teal)"/><path d="M7 5l2 2.5-1.2 1.2a7 7 0 0 0 3.5 3.5L12.5 11l2.5 2-1.2 1.7C10 14.5 5.5 10 5.3 6.2z" fill="#fff"/></svg>
      801-555-0187
    </span>
  </div>

  <div class="contact-row secondary">
    <span class="contact-item">
      <svg class="icon" viewBox="0 0 20 20"><circle cx="10" cy="10" r="10" fill="var(--teal)"/><rect x="6" y="5" width="8" height="10" rx="1" fill="#fff"/><rect x="7.5" y="7" width="5" height="3" fill="var(--teal)"/></svg>
      888-555-0163
    </span>
    <span class="contact-item">
      <svg class="icon" viewBox="0 0 20 20"><circle cx="10" cy="10" r="10" fill="var(--teal)"/><rect x="5" y="6.5" width="10" height="7" fill="#fff"/><path d="M5 6.5l5 4 5-4" fill="none" stroke="var(--teal)" stroke-width="1"/></svg>
      ashworthderek385@mailnest.example
    </span>
    <span class="contact-item">
      <svg class="icon" viewBox="0 0 20 20"><circle cx="10" cy="10" r="10" fill="var(--teal)"/><circle cx="10" cy="10" r="5" fill="none" stroke="#fff" stroke-width="1.3"/><ellipse cx="10" cy="10" rx="2" ry="5" fill="none" stroke="#fff" stroke-width="1.1"/><line x1="5" y1="10" x2="15" y2="10" stroke="#fff" stroke-width="1.1"/></svg>
      www.derekashworthteam.example
    </span>
  </div>

  <div class="bottom-band"></div>
  <div class="web-tab">www.DerekAshworthTeam.example</div>
</div>
</body>
</html>
```